Walk Bold Stay Kind Ebook and Print book cover

I need a professional, eye catching cover that will stand out. The title of the book is "Walk Bold Stay Kind: 47 Quiet Rules For Calm and Wonder" It is a self-help personal transformation book by author Dale Ormsby. The cover will be on both print and ebook covers. I want something that is similar yet different to best-selling books in the genre, nothing too boring. A blue background might work, but it isn't a requirement. I'm open to other colors as long as it's powerful, professional, and screams "Buy me because this book is going to change your life!"
Updates

So far, 3 designs (3 of the 4 star rated designs) are in contention, but they all can be improved. I think the book cover should best convey "thinking smart" in a dynamic way. I'll run another poll in a day or so when I get additional designs I like. Added Thursday, May 4, 2017

Based on current designs, I wanted to provide additional guidance. The title and image should pop and be clearly visible at a distance as a thumbnail. Also, I'm wanting something bold and creative but not too confusing. I currently have a couple solid designs that are in contention to win, but I have another 7 days left for the project. I extended it to 10 days from the initial 5. I'll include several more polls for my followers and will likely pick the top ranking design based off the series of polls and will be eliminating lower ranking designs with each new poll and set of promising designs that come in. Finally, I may ask to see what the back will look like on the print version since I'll need both the Lumora and print (5" by 8") designs. Added Saturday, May 6, 2017

It's been recommended by some that I should have my own picture on the cover. I'm not completely convinced, but I would like to see some additional designs that incorporate my photo (touched up to remove the shine from my forehead and the label brand name removed from the t-shire) into a cover design. I have several good designs coming in, so typeset and professional looking font is extremely important. Blue is also preferred but not required. I've attached the photo on the brief for those who want to submit a design with that photo. Added Saturday, May 6, 2017

Target Market(s)

Working age adults seeking personal transformation and self improvement.

Industry/Entity Type

Motivation

Requirements
Must have
• Creativity. Eye catching. Striking. Contrast. Looks good close up and as a thumbnail at a distance. Font should be easy to read and pop from the cover along with the design.
Nice to have
• Powerful image placement. Play up the "Walk Bold" aspect of the title. Perhaps even contrasting someone who's thinking "Hard." Here are a few examples of intriguing covers (though not necessarily related to the genre) I like mainly for aesthetics and creativity. https://www.shopvale.com/dp/Q71MRT2KWD/ https://www.shopvale.com/dp/Q34PLN8XEA
• https://www.shopvale.com/dp/Q925GHV3TC/
• https://www.shopvale.com/dp/Q48DJW6RZB/
• (the font is a little poor in the last one but the image is evoking)
Should not have
• Ugly, tacky, or hard to read fonts. A simple photo with text on top. A simple background with words. Confusing images. Designs with no additional stock image purchase requirements will be given preference over those that do. I've seen a lot of balloons and light bulbs. I'm not saying you can't include them in the design, but if you want to stand out, try to find something more creative that expresses the concept of the title.

```html
<!DOCTYPE html>
<html lang="en">
<head>
<meta charset="utf-8">
<title>Walk Bold Stay Kind — Dale Ormsby</title>
<link href="https://fonts.googleapis.com/css2?family=Tinos:ital,wght@0,700;1,700&display=swap" rel="stylesheet">
<style>
  :root {
    --navy-deep: #0a1f45;
    --navy: #0d2f6b;
    --royal: #0b4d9c;
    --royal-light: #1466b8;
    --cream: #d6d4c0;
    --cream-soft: #c9c7b0;
    --line: #d8d5bf;
    --glow: #f4f2e4;
  }
  * { margin: 0; padding: 0; box-sizing: border-box; }
  html, body {
    width: 960px;
    height: 1200px;
    overflow: hidden;
    background: var(--navy-deep);
  }
  .cover {
    position: relative;
    width: 960px;
    height: 1200px;
    overflow: hidden;
    font-family: "Tinos", "Times New Roman", serif;
  }
  .cover-art {
    position: absolute;
    inset: 0;
    width: 960px;
    height: 1200px;
  }
  .title {
    position: absolute;
    left: 0;
    right: 0;
    top: 70px;
    color: var(--cream);
    font-style: italic;
    font-weight: 700;
    font-size: 150px;
    line-height: 0.88;
    letter-spacing: -1px;
    text-shadow: 2px 3px 4px rgba(0, 0, 0, 0.35);
  }
  .title-line { display: block; }
  .title-line--first { padding-left: 120px; }
  .title-line--second { padding-left: 210px; }
  .subtitle {
    position: absolute;
    left: 0;
    right: 0;
    top: 948px;
    text-align: center;
    color: var(--cream);
    font-style: italic;
    font-weight: 700;
    font-size: 34px;
    letter-spacing: 0.3px;
  }
  .author {
    position: absolute;
    left: 0;
    right: 0;
    top: 1100px;
    text-align: center;
    color: var(--cream-soft);
    font-weight: 700;
    font-size: 44px;
    letter-spacing: 2px;
    text-transform: uppercase;
  }
</style>
</head>
<body>
<main class="cover">
  <svg class="cover-art" viewBox="0 0 960 1200" xmlns="http://www.w3.org/2000/svg">
    <defs>
      <radialGradient id="field" cx="0.55" cy="0.5" r="0.75">
        <stop offset="0" stop-color="#0f3a80"/>
        <stop offset="0.6" stop-color="#0c2b62"/>
        <stop offset="1" stop-color="#081a3d"/>
      </radialGradient>
      <linearGradient id="sweep-top" x1="0" y1="0" x2="1" y2="1">
        <stop offset="0" stop-color="#0d4fa0"/>
        <stop offset="1" stop-color="#0a3e86"/>
      </linearGradient>
      <linearGradient id="sweep-bottom" x1="0" y1="0" x2="1" y2="1">
        <stop offset="0" stop-color="#0b58ad"/>
        <stop offset="1" stop-color="#0a3f8a"/>
      </linearGradient>
      <radialGradient id="figure-glow" cx="0.5" cy="0.5" r="0.5">
        <stop offset="0" stop-color="#d9d7c2"/>
        <stop offset="0.72" stop-color="#cfcdb6"/>
        <stop offset="0.88" stop-color="#e9e7d6" stop-opacity="0.7"/>
        <stop offset="1" stop-color="#f4f2e4" stop-opacity="0"/>
      </radialGradient>
    </defs>

    <rect class="field" width="960" height="1200" fill="url(#field)"/>

    <!-- upper right light sweep -->
    <path class="sweep sweep--top" d="M420 0 C 600 120, 800 300, 960 560 L960 0 Z" fill="url(#sweep-top)"/>
    <!-- lower left light sweep -->
    <path class="sweep sweep--bottom" d="M0 840 C 140 1000, 300 1110, 520 1200 L0 1200 Z" fill="url(#sweep-bottom)"/>

    <!-- fine cream curves -->
    <path class="rule" d="M420 0 C 600 120, 800 300, 960 560" fill="none" stroke="var(--line)" stroke-width="2"/>
    <path class="rule" d="M0 840 C 140 1000, 300 1110, 520 1200" fill="none" stroke="var(--line)" stroke-width="2"/>

    <!-- frame lines -->
    <line class="rule" x1="168" y1="330" x2="168" y2="1000" stroke="var(--line)" stroke-width="2"/>
    <line class="rule" x1="168" y1="1000" x2="960" y2="1000" stroke="var(--line)" stroke-width="2"/>
    <line class="rule" x1="600" y1="700" x2="900" y2="1000" stroke="var(--line)" stroke-width="2"/>

    <!-- central figure area -->
    <rect class="figure" x="230" y="360" width="560" height="540" rx="200"
          fill="url(#figure-glow)" role="img"
          aria-label="Profile silhouette of a head whose brain holds a chessboard with chess pieces"/>
  </svg>

  <h1 class="title">
    <span class="title-line title-line--first">Walk Bold</span>
    <span class="title-line title-line--second">Stay Kind</span>
  </h1>

  <p class="subtitle">47 Quiet Rules For Calm and Wonder</p>

  <p class="author">Dale Ormsby</p>
</main>
</body>
</html>
```